App "loading/waiting" animated GIF

We need an original "loading/waiting" animated GIF to fit our desktop app design (linked)
The app logo and the hexagon shape could be an inspiration source, "Artificial Intelligence" is the main topic of this app.
In general the user have to wait between 1s and 10s
The GIF should fit inside a 300px square (with a 2x resolution version)

Colors
33a6d7
0455a3

```html
<!DOCTYPE html>
<html lang="en">
<head>
<meta charset="utf-8">
<title>Loading indicator</title>
<link href="https://fonts.googleapis.com/css2?family=Fira+Sans:wght@600&display=swap" rel="stylesheet">
<style>
  :root {
    --bg: #000000;
    --blue-light: #33a6d7;
    --blue-deep: #0455a3;
  }
  html, body {
    margin: 0;
    padding: 0;
    width: 1200px;
    height: 1200px;
    overflow: hidden;
    background: var(--bg);
  }
  .loader {
    display: block;
    width: 1200px;
    height: 1200px;
  }
  .hex-stroke {
    fill: none;
    stroke-width: 3;
    stroke-linecap: round;
    stroke-linejoin: round;
  }
  .hex-stroke--light { stroke: var(--blue-light); }
  .hex-stroke--deep { stroke: var(--blue-deep); }
  .status-label {
    font-family: "Fira Sans", sans-serif;
    font-weight: 600;
    font-size: 20px;
    fill: var(--blue-light);
    letter-spacing: 0.3px;
  }
  .progress-track {
    fill: none;
    stroke: var(--blue-light);
    stroke-width: 1.6;
  }
</style>
</head>
<body>
<svg class="loader" viewBox="0 0 600 600" xmlns="http://www.w3.org/2000/svg">
  <g class="hexagon">
    <path class="hex-stroke hex-stroke--deep" d="M277,134 L234,157"/>
    <path class="hex-stroke hex-stroke--light" d="M234,157 L190,184 Q186,187 186,193 L185,232"/>

    <path class="hex-stroke hex-stroke--light" d="M301,123 L388,172"/>
    <path class="hex-stroke hex-stroke--deep" d="M388,172 L408,184 Q412,187 413,193 L414,208"/>

    <path class="hex-stroke hex-stroke--light" d="M414,258 L413,313 Q412,319 406,322 L378,339"/>
    <path class="hex-stroke hex-stroke--deep" d="M378,339 L334,364"/>

    <path class="hex-stroke hex-stroke--light" d="M288,376 L203,327"/>
    <path class="hex-stroke hex-stroke--deep" d="M203,327 L193,321 Q188,318 187,312 L186,283"/>
  </g>

  <text class="status-label" x="300" y="255" text-anchor="middle">initializing...</text>

  <rect class="progress-track" x="128" y="416" width="343" height="23"/>
</svg>
</body>
</html>
```